Plovetta Cyberline Solutions- Computer Network Company

Wordpress designs.

I want a web design that is up scale looking, high-end. A very modern and clean looking.

Thinking of rotating pictures of Network Management (picture of server/desktop computer), Backup Solutions (picture of server after fire), Network wiring (picture maybe of racks/switches, etc)

Service- Backup Solutions, Managing computers and servers, Database management, Network Wiring, Phone system management

Products we sell Vornix computers, QT printers,
About the company
Contact us

Target Market(s)

Companies looking for Computer support, Law office, Private business

Industry/Entity Type

Computer

Coding

Coded - Design and coding required

Font styles to use
Sans Serif

Requirements
Must have
• Wordpress design, will be hosted on a Linux server.
• Use the logo in the design, Clean, Up scale website
• Navigation- Services-Products -About Us-Contact Us
• ***Also, a link for Buying a domain (we are a reseller of hosting and domain names)*****
Nice to have
• picture rotation on the landing page, Network Management,

```html
<!DOCTYPE html>
<html lang="en">
<head>
<meta charset="utf-8">
<title>Plovetta Cyberline Solutions</title>
<link rel="stylesheet" href="https://fonts.googleapis.com/css2?family=Exo+2:wght@500;600;700&family=Lato:wght@400;700&display=swap">
<style>
:root{
  --navy:#1d3c8c;
  --navy-dark:#15245a;
  --green:#0f5a38;
  --green-dark:#0c4a2e;
  --text:#333;
  --muted:#555;
  --grey-bg:#f3f3f3;
  --footer:#222;
  --line:#dcdcdc;
  --white:#fff;
}
*{box-sizing:border-box;margin:0;padding:0}
html,body{width:1200px;height:2571px;overflow:hidden}
body{font-family:"Lato",sans-serif;color:var(--text);background:var(--white);position:relative}
h1,h2,h3,h4,.brand{font-family:"Exo 2",sans-serif}

/* header */
.site-header{position:relative;height:115px;background:linear-gradient(#fff,#f4f4f4);border-bottom:1px solid #e4e4e4}
.top-bar{position:absolute;right:0;top:0;width:437px;height:38px;background:var(--navy);clip-path:polygon(30px 0,100% 0,100% 100%,0 100%);display:flex;align-items:center;justify-content:flex-end;gap:34px;padding-right:98px;color:#fff;font-size:13px;font-weight:700}
.top-bar span{display:flex;align-items:center;gap:10px}
.top-bar .ico{width:22px;height:22px;border-radius:50%;background:rgba(255,255,255,.18);display:flex;align-items:center;justify-content:center}
.brand-mark{position:absolute;left:98px;top:34px;display:flex;align-items:center;gap:12px}
.brand-mark .dot{width:40px;height:40px;border-radius:50%;background:var(--navy)}
.brand-mark .brand{font-size:21px;font-weight:700;color:var(--navy);line-height:1.1;width:200px}
.main-nav{position:absolute;right:98px;top:74px;display:flex;gap:50px;font-size:14px;color:#444}
.main-nav a{color:inherit;text-decoration:none;position:relative}
.main-nav a.active{color:var(--green);font-weight:700}
.main-nav a.active::after{content:"";position:absolute;left:0;right:0;bottom:-20px;height:3px;background:var(--green)}

/* hero */
.hero{position:relative;height:557px}
.hero-photo{position:absolute;inset:0;background:radial-gradient(circle at 50% 40%,#c9d3de 0%,#7f8fa0 40%,#3c4652 80%,#22272e 100%)}
.hero-arrow{position:absolute;transform:translateY(-50%)}
.hero-arrow.prev{left:22px;top:370px}
.hero-arrow.next{right:22px;top:370px}
.hero-caption{position:absolute;left:0;right:0;bottom:0;height:58px;background:rgba(30,30,30,.72);display:flex;align-items:center;padding-left:101px}
.hero-caption h1{color:#fff;font-size:30px;font-weight:600}
.hero-dots{position:absolute;right:98px;bottom:22px;display:flex;gap:8px}
.hero-dots i{width:12px;height:12px;border-radius:50%;background:#aaa}
.hero-dots i.on{background:#4a7bd0}

/* services */
.services{height:368px;padding:55px 0 0 98px;display:grid;grid-template-columns:repeat(3,366px);row-gap:36px;align-content:start}
.service{display:flex;gap:12px}
.service .icon{flex:0 0 56px;height:56px;border-radius:50%;border:3px solid #d0d7e6;background:var(--navy);display:flex;align-items:center;justify-content:center}
.service h3{font-size:18px;font-weight:600;color:var(--navy);line-height:1.15;margin-top:2px}
.service p{font-size:12.5px;line-height:1.5;color:var(--muted);margin-top:12px;width:180px}

/* products */
.products{height:312px;background:var(--grey-bg);display:flex;gap:50px;padding:52px 0 0 98px}
.product{width:476px;height:209px;border-radius:8px;display:flex;align-items:center;color:#fff;overflow:hidden}
.product.printers{background:var(--navy)}
.product.computers{background:var(--green)}
.product .shot{width:255px;height:209px}
.printers .shot{background:linear-gradient(135deg,#e6e6e6,#9a9a9a)}
.computers .shot{background:linear-gradient(135deg,#4a8ad8,#2b2b2b)}
.product h2{font-size:29px;font-weight:600;line-height:1.2}
.product p{font-size:12.5px;line-height:1.55;margin-top:12px;width:180px}
.product .body{padding-left:20px}

/* why */
.why{position:relative;height:563px;color:#fff;text-align:center}
.why-bg{position:absolute;inset:0;background:linear-gradient(#1b2a6a 0%,#1c2e6c 45%,#30477e 75%,#1d2b5e 100%)}
.why .inner{position:relative}
.section-title{font-size:35px;font-weight:700;padding-top:42px}
.rule{display:flex;align-items:center;justify-content:center;margin:12px auto 0;width:420px}
.rule::before,.rule::after{content:"";flex:1;height:1px;background:rgba(255,255,255,.45)}
.rule .globe{width:20px;height:20px;border-radius:50%;background:#3a7ad0;margin:0 8px}
.why .lead{font-size:17px;margin-top:14px}
.why-hub{position:absolute;left:489px;top:234px;width:220px;height:220px;border-radius:50%;background:#fff;border:8px solid #c6cbd6;display:flex;align-items:center;justify-content:center}
.why-hub .brand{color:var(--navy);font-size:19px;font-weight:700;line-height:1.15;width:150px}
.feature{position:absolute}
.feature h3{font-size:18px;font-weight:600}
.feature p{font-size:12.5px;line-height:1.55;margin-top:6px}
.feature.left{text-align:right}
.feature.right{text-align:left}
.feature .ring{position:absolute;top:2px;width:56px;height:56px;border-radius:50%;border:2px solid #fff;display:flex;align-items:center;justify-content:center}
.feature.left .ring{right:-72px}
.feature.right .ring{left:-72px}
.f1{left:100px;top:252px;width:205px}
.f2{left:100px;top:382px;width:205px}
.f3{left:884px;top:252px;width:205px}
.f4{left:884px;top:382px;width:205px}
.connectors{position:absolute;left:0;top:0}

/* partners */
.partners{height:284px;background:#f5f5f5;text-align:center}
.partners .section-title{color:#111;padding-top:42px}
.partners .section-title em{font-style:normal;color:var(--green)}
.partners .rule::before,.partners .rule::after{background:#bbb}
.partner-row{display:flex;gap:26px;justify-content:center;margin-top:30px}
.partner{width:144px;height:74px;background:#fff;border:1px solid var(--line);display:flex;align-items:center;justify-content:center}
.partner i{width:90px;height:24px;border-radius:4px;background:#cfcfcf}

/* footer */
.site-footer{height:321px;background:var(--footer);color:#ccc;display:flex;padding:50px 0 0 98px;font-size:13px}
.site-footer h4{color:#fff;font-size:18px;font-weight:600;letter-spacing:.5px}
.site-footer h4::after{content:"";display:block;width:36px;height:2px;background:#888;margin-top:12px}
.links{width:168px}
.links ul{list-style:none;margin-top:14px}
.links li{line-height:28px}
.links li::before{content:"›";margin-right:8px;color:#888}
.contact{width:298px}
.contact h4::after{width:260px;height:1px;background:#555}
.contact strong{display:block;color:#fff;font-size:15px;margin-top:16px}
.contact p{line-height:1.6;margin-top:4px}
.contact .row{display:flex;align-items:center;gap:12px;margin-top:10px}
.quick{width:258px}
.quick h4::after{width:258px;height:1px;background:#555}
.quick .field{background:#fff;color:#777;height:34px;padding:9px 10px;margin-top:9px;font-size:12px}
.quick .field:first-of-type{margin-top:18px}
.quick .field.tall{height:52px}
.quick .submit{display:inline-block;background:var(--green);color:#fff;font-weight:700;padding:10px 24px;margin-top:10px;font-size:13px}
.foot-brand{margin-left:56px;margin-top:78px;text-align:center;width:224px}
.foot-brand .brand{color:#ddd;font-size:20px;font-weight:700;line-height:1.15}
.socials{display:flex;gap:10px;justify-content:center;margin-top:16px}
.socials i{width:30px;height:30px;border-radius:50%}
.copyright{height:51px;background:var(--green-dark);color:#ddd;font-size:13px;display:flex;align-items:center;justify-content:center}
</style>
</head>
<body>

<header class="site-header">
  <div class="top-bar">
    <span><span class="ico"><svg width="12" height="12" viewBox="0 0 24 24"><path fill="#fff" d="M6.6 10.8a15 15 0 006.6 6.6l2.2-2.2c.3-.3.7-.4 1-.2 1.1.4 2.3.6 3.6.6.6 0 1 .4 1 1V20c0 .6-.4 1-1 1A17 17 0 013 4c0-.6.4-1 1-1h3.5c.6 0 1 .4 1 1 0 1.3.2 2.5.6 3.6.1.3 0 .7-.2 1z"/></svg></span>123.555.0190</span>
    <span><span class="ico"><svg width="12" height="10" viewBox="0 0 24 18"><path fill="#fff" d="M0 0h24v18H0zM2 2l10 7 10-7z"/></svg></span>hello@plovetta-cyber.com</span>
  </div>
  <div class="brand-mark"><span class="dot"></span><span class="brand">Plovetta Cyberline Solutions</span></div>
  <nav class="main-nav">
    <a class="active" href="#">Home</a><a href="#">About Us</a><a href="#">Services</a><a href="#">Products</a><a href="#">Domain &amp; Hosting</a><a href="#">Contact Us</a>
  </nav>
</header>

<section class="hero">
  <div class="hero-photo" role="img" aria-label="Hand reaching toward a glowing network of cloud, server, database and device icons over a server room"></div>
  <svg class="hero-arrow prev" width="20" height="40" viewBox="0 0 20 40"><path d="M18 2L2 20l16 18" stroke="#fff" stroke-width="2" fill="none"/></svg>
  <svg class="hero-arrow next" width="20" height="40" viewBox="0 0 20 40"><path d="M2 2l16 18L2 38" stroke="#fff" stroke-width="2" fill="none"/></svg>
  <div class="hero-caption"><h1>We Are The Leaders in Computer Networking business</h1></div>
  <div class="hero-dots"><i class="on"></i><i></i><i></i></div>
</section>

<section class="services">
  <div class="service"><span class="icon"><svg width="26" height="26" viewBox="0 0 24 24"><circle cx="12" cy="12" r="9" stroke="#fff" stroke-width="2" fill="none"/><path d="M12 7v5l3 3" stroke="#fff" stroke-width="2" fill="none"/></svg></span><div><h3>Backup<br>Solutions</h3><p>Sed ut perspiciatis unde omnis iste natus is error the sit. lorem ipsum the isSed ut.</p></div></div>
  <div class="service"><span class="icon"><svg width="24" height="26" viewBox="0 0 24 26"><rect x="3" y="2" width="18" height="6" fill="#fff"/><rect x="3" y="10" width="18" height="6" fill="#fff"/><rect x="3" y="18" width="18" height="6" fill="#fff"/></svg></span><div><h3>Managing Servers /<br>Workstations</h3><p>Sed ut perspiciatis unde omnis iste natus is error the sit. lorem ipsum the isSed ut.</p></div></div>
  <div class="service"><span class="icon"><svg width="22" height="26" viewBox="0 0 22 26"><ellipse cx="11" cy="5" rx="9" ry="3.5" fill="#fff"/><path d="M2 9c0 2 4 3.5 9 3.5S20 11 20 9v5c0 2-4 3.5-9 3.5S2 16 2 14zM2 18c0 2 4 3.5 9 3.5s9-1.5 9-3.5v3c0 2-4 3.5-9 3.5S2 23 2 21z" fill="#fff"/></svg></span><div><h3>Database<br>Management</h3><p>Sed ut perspiciatis unde omnis iste natus is error the sit. lorem ipsum the isSed ut.</p></div></div>
  <div class="service"><span class="icon"><svg width="26" height="26" viewBox="0 0 24 24"><path d="M4 17h10a4 4 0 000-8H8a3 3 0 010-6h12" stroke="#fff" stroke-width="2" fill="none"/></svg></span><div><h3>Network<br>Wiring</h3><p>Sed ut perspiciatis unde omnis iste natus is error the sit. lorem ipsum the isSed ut.</p></div></div>
  <div class="service"><span class="icon"><svg width="24" height="26" viewBox="0 0 24 26"><rect x="2" y="3" width="6" height="20" rx="2" fill="#fff"/><rect x="10" y="5" width="12" height="18" rx="1" fill="#fff"/><rect x="12" y="8" width="8" height="3" fill="#1d3c8c"/></svg></span><div><h3>Phone<br>Systems</h3><p>Sed ut perspiciatis unde omnis iste natus is error the sit. lorem ipsum the isSed ut.</p></div></div>
  <div class="service"><span class="icon"><svg width="24" height="26" viewBox="0 0 24 26"><circle cx="12" cy="9" r="6" fill="#fff"/><path d="M2 25c1-6 5-9 10-9s9 3 10 9z" fill="#fff"/></svg></span><div><h3>Remote<br>Support</h3><p>We use an easy-to-use, customizable solution that provides premier remote.</p></div></div>
</section>

<section class="products">
  <div class="product printers"><div class="shot" role="img" aria-label="Office laser printer"></div><div class="body"><h2>QT<br>Printers</h2><p>Sed ut perspiciatis unde omnis iste natus is error the sit. lorem ipsum the isSed ut.</p></div></div>
  <div class="product computers"><div class="shot" role="img" aria-label="Open laptop with a tiled start screen"></div><div class="body"><h2>Vornix<br>Computers</h2><p>Sed ut perspiciatis unde omnis iste natus is error the sit. lorem ipsum the isSed ut.</p></div></div>
</section>

<section class="why">
  <div class="why-bg" role="img" aria-label="Dark blue data-centre corridor with streams of binary code"></div>
  <div class="inner">
    <h2 class="section-title">WHY CHOOSE US</h2>
    <div class="rule"><span class="globe"></span></div>
    <p class="lead">We Are A Leading Construction Management &amp; Engineering Company</p>
  </div>
  <svg class="connectors" width="1200" height="563">
    <g stroke="rgba(255,255,255,.6)" fill="#fff">
      <line x1="405" y1="264" x2="500" y2="264"/><line x1="405" y1="394" x2="500" y2="394"/>
      <line x1="700" y1="264" x2="795" y2="264"/><line x1="700" y1="394" x2="795" y2="394"/>
      <circle cx="405" cy="264" r="5"/><circle cx="405" cy="394" r="5"/>
      <circle cx="795" cy="264" r="5"/><circle cx="795" cy="394" r="5"/>
    </g>
  </svg>
  <div class="why-hub"><span class="brand">Plovetta Cyberline Solutions</span></div>
  <div class="feature left f1"><h3>Certified Experience</h3><p>Lorem ipsum dolor sit amet consectetuer Lorem ipsum dolor sit amet adipiscing el ...</p><span class="ring"><svg width="24" height="28" viewBox="0 0 24 28"><path d="M4 2h11l5 5v19H4z" stroke="#fff" stroke-width="2" fill="none"/></svg></span></div>
  <div class="feature left f2"><h3>Competitive Pricing</h3><p>Lorem ipsum dolor sit amet consectetuer Lorem ipsum dolor sit amet adipiscing el ...</p><span class="ring"><svg width="28" height="24" viewBox="0 0 28 24"><circle cx="19" cy="12" r="8" stroke="#fff" stroke-width="2" fill="none"/><path d="M2 12h6v10H2z" fill="#fff"/></svg></span></div>
  <div class="feature right f3"><h3>Highly Professionals</h3><p>Lorem ipsum dolor sit amet, consectetuer Lorem ipsum dolor sit amet adipiscing el ...</p><span class="ring"><svg width="30" height="22" viewBox="0 0 30 22"><circle cx="15" cy="6" r="5" fill="#fff"/><circle cx="6" cy="8" r="4" fill="#fff"/><circle cx="24" cy="8" r="4" fill="#fff"/><path d="M6 22c0-6 4-9 9-9s9 3 9 9z" fill="#fff"/></svg></span></div>
  <div class="feature right f4"><h3>100% Satisfaction</h3><p>Lorem ipsum dolor sit amet, consectetuer Lorem ipsum dolor sit amet adipiscing el ...</p><span class="ring"><svg width="22" height="28" viewBox="0 0 22 28"><circle cx="11" cy="10" r="8" stroke="#fff" stroke-width="2" fill="none"/><path d="M6 17l-2 10 7-4 7 4-2-10" fill="#fff"/></svg></span></div>
</section>

<section class="partners">
  <h2 class="section-title">OUR <em>PARTNERS</em></h2>
  <div class="rule"><span class="globe"></span></div>
  <div class="partner-row">
    <div class="partner"><i></i></div><div class="partner"><i></i></div><div class="partner"><i></i></div>
    <div class="partner"><i></i></div><div class="partner"><i></i></div><div class="partner"><i></i></div>
  </div>
</section>

<footer class="site-footer">
  <div class="links"><h4>QUICK LINKS</h4>
    <ul><li>Home</li><li>About Us</li><li>Services</li><li>Products</li><li>Domain &amp; Hosting</li><li>Contact Us</li></ul>
  </div>
  <div class="contact"><h4>CONTACT DETAILS</h4>
    <strong>PLOVETTA</strong>
    <p>48 Harbor Loop Avenue, Suite 210,<br>Fernwick - 902 117</p>
    <div class="row"><svg width="14" height="14" viewBox="0 0 24 24"><path fill="#ddd" d="M6.6 10.8a15 15 0 006.6 6.6l2.2-2.2c.3-.3.7-.4 1-.2 1.1.4 2.3.6 3.6.6.6 0 1 .4 1 1V20c0 .6-.4 1-1 1A17 17 0 013 4c0-.6.4-1 1-1h3.5c.6 0 1 .4 1 1 0 1.3.2 2.5.6 3.6.1.3 0 .7-.2 1z"/></svg>123.555.0190</div>
    <div class="row"><svg width="14" height="14" viewBox="0 0 24 24"><path fill="#ddd" d="M6 2h12v5H6zM2 8h20v10h-4v4H6v-4H2z"/></svg>123.555.0190</div>
    <div class="row"><svg width="14" height="11" viewBox="0 0 24 18"><path fill="#ddd" d="M0 0h24v18H0zM2 2l10 7 10-7z"/></svg>hello@plovetta-cyber.com</div>
  </div>
  <div class="quick"><h4>QUICK CONTACT</h4>
    <div class="field">Name</div><div class="field">Email</div><div class="field tall">How We Can Help You?</div>
    <span class="submit">SUBMIT</span>
  </div>
  <div class="foot-brand"><span class="brand">Plovetta Cyberline Solutions</span>
    <div class="socials"><i style="background:#3b5998"></i><i style="background:#2fa6d8"></i><i style="background:#1a76b4"></i><i style="background:#d3322a"></i></div>
  </div>
</footer>
<div class="copyright">Copyright © 2016 Plovetta. All Rights Reserved.</div>

</body>
</html>
```